velmorino.eu :: Design ideas (no coding) for key pages of Personalized greeting cards online store

We need your vision on modern, clean, easy to read user interface (UI) for online service of personalized printed products, like greeting cards, postcards, fridge magnets, clips and etc.
Your vision should include UI presentation for:
- Home page with login (including soc nets)
- Product Designer page
- Cart pages (products and address selection)
- Example of general internal page (pricing, terms, etc)
- Artist info and portfolio page
We are looking for ideas we will love, NOT complete design of a whole site.
Top design/vision will we used as a basement for separate contract on complete design of the site.

UI should be based on existing functionality with some extent. It should not break ideas or methods used on prototype but designers are free to offer own product presentations, designer’s layout and cart views.

Prototype:
English: http://velmorino.eu
Russian: http://velmorino.ru
Lithuanian: http://velmorino.lt

Target Market(s)

People of 16-45 y.o. who likes to be distinctive, personal.

Industry/Entity Type

Store

Requirements
Must have
• Your work should meet attached requirements.
Site is multilingual. Wording should assume varieties in length on different languages.
Clean and easy to read UI
Flat design preferrably
Should be based on assets which are free or available for royalty-free licensing
Should not have
• heavy, meaningless 3D and shadow effects
Show NOT copy sites like: plonkra.com, tarnwick.co.uk

```html
<!DOCTYPE html>
<html lang="en">
<head>
<meta charset="utf-8">
<title>Velmorino — Greeting Cards</title>
<link href="https://fonts.googleapis.com/css2?family=Open+Sans:wght@400;600;700&family=Montserrat:wght@400;500&display=swap" rel="stylesheet">
<style>
:root{
  --paper:#fbf9ef;
  --banner:#fdf3e3;
  --banner-text:#7a5a3a;
  --ink:#3d3d3d;
  --red:#d8443a;
  --red-dark:#b52a22;
  --navy:#2e5a84;
  --teal:#1e8b8b;
  --tab-border:#d6d3c6;
  --price:#c0302a;
  --sky:#1a9fd0;
  --sun:#fdc934;
  --footer:#efefef;
  --peach:#f7c382;
}
*{box-sizing:border-box;margin:0;padding:0}
html,body{width:924px;height:1200px;overflow:hidden}
body{background:var(--paper);font-family:"Open Sans",sans-serif;color:var(--ink);position:relative}
.abs{position:absolute}
.top-banner{left:0;top:0;width:924px;height:39px;background:var(--banner);border-bottom:1px solid #eadcc4;text-align:center;font-size:18px;line-height:39px;color:var(--banner-text)}
.brand{left:92px;top:50px;width:60px;text-align:center}
.brand-mark{width:44px;height:44px;margin:0 auto;background:var(--red);border-radius:4px}
.brand-name{font-size:11px;color:var(--red-dark);margin-top:3px}
.main-nav{right:268px;top:73px;font-size:12px;line-height:16px;color:#555;display:flex;gap:11px;white-space:nowrap}
.main-nav .sep{color:#bbb}
.btn-cart{left:666px;top:69px;width:89px;height:25px;background:var(--red-dark);color:#fff;font-size:10px;font-weight:600;padding-left:10px;display:flex;gap:6px;align-items:center;white-space:nowrap}
.btn-checkout{left:755px;top:69px;width:76px;height:25px;background:var(--navy);color:#fff;font-size:10px;font-weight:600;line-height:25px;text-align:center;white-space:nowrap}
.tabs{left:92px;top:121px;width:739px;height:30px;border:1px solid var(--tab-border);border-bottom:none;display:flex;background:#fff}
.tabs div{padding:0 12px;font-size:12px;line-height:29px;border-right:1px solid var(--tab-border);white-space:nowrap}
.tabs .fav{margin-left:auto;background:var(--red);color:#fff;border-right:none;width:126px;text-align:center;font-weight:600}
.hero{left:92px;top:151px;width:739px;height:244px;background:linear-gradient(120deg,#c9c3bb 0%,#eae6e1 35%,#d94d3a 70%,#e8b23c 100%)}
.hero-panel{left:92px;top:203px;width:332px;height:151px;background:rgba(40,40,40,.72);padding:14px 22px;color:#fff}
.hero-panel h1{font-family:"Montserrat",sans-serif;font-weight:400;font-size:25px;margin-bottom:8px;white-space:nowrap}
.hero-panel p{font-size:10px;line-height:13px}
.hero-btn{display:inline-block;margin-top:14px;margin-left:4px;background:var(--peach);color:#5a3a1a;font-size:11px;padding:4px 18px}
.arrow{top:251px;width:46px;height:46px;border-radius:50%;background:var(--teal)}
.section-label{font-size:12px;color:#333}
.themes-line{left:92px;top:435px;width:600px;border-top:1px solid #ddd}
.colors-line{left:714px;top:435px;width:112px;border-top:1px solid #ddd}
.btn-more{left:638px;top:417px;width:55px;height:18px;background:var(--red);color:#fff;font-size:10px;line-height:18px;text-align:center}
.tag-line{left:92px;font-size:10.5px;line-height:18px;display:flex;align-items:center;gap:9px;white-space:nowrap}
.tag-line .b{font-weight:700;font-size:11.5px}
.tag-line .big{font-size:12.5px}
.tag-line .sel{background:var(--teal);color:#fff;padding:0 6px}
.swatch{top:445px;width:52px;height:32px}
.reset{left:714px;top:486px;width:112px;height:18px;border:1px solid var(--red);background:#fff;font-size:9px;color:var(--red);line-height:16px;white-space:nowrap}
.reset i{display:inline-block;width:16px;height:16px;background:var(--red);color:#fff;font-style:normal;text-align:center;margin-right:14px}
.card{width:161px;height:207px;background:#fff;border:1px solid #e3e0d5}
.card .art{height:167px}
.card .strip{height:5px;background:linear-gradient(90deg,#3b3d8f 0 10%,#e84a2f 10% 20%,#1f8fd6 20% 30%,#f59b2b 30% 40%,#f7c94a 40% 50%,#d6d6d6 50% 60%,#e06f3a 60% 70%,#8b8b8b 70% 80%,#3c8a3a 80% 90%,#f59b2b 90% 100%)}
.card .meta{display:flex;align-items:center;height:34px;padding:0 7px}
.price{font-weight:700;font-size:11.5px;color:var(--price);flex:1}
.icons{display:flex;gap:10px}
.loading{left:0;top:1003px;width:924px;text-align:center;font-size:9px;color:#555}
.footer{left:0;top:1058px;width:924px;height:142px;background:var(--footer)}
.footer-links{left:0;top:1081px;width:924px;text-align:center;font-size:9px;color:#555;white-space:nowrap}
.footer-links span{margin:0 5px}
.footer-links .dot{color:#bbb;margin:0}
.social{left:403px;top:1112px;display:flex;gap:4px}
.social div{width:23px;height:23px;background:#e4e4e4}
.social .on{background:#55c3ef}
.copy{left:0;top:1156px;width:924px;text-align:center;font-size:8px;color:#666}
</style>
</head>
<body>
<div class="abs top-banner">The individual greeting cards according to your mood</div>

<div class="abs brand"><div class="brand-mark"></div><div class="brand-name">Velmorino</div></div>

<nav class="abs main-nav"><span>Products</span><span class="sep">|</span><span>Authors</span><span class="sep">|</span><span>Sign In</span></nav>
<div class="abs btn-cart"><svg width="13" height="11" viewBox="0 0 13 11"><path d="M0 1h2l2 6h7l1.5-5H3" fill="none" stroke="#fff" stroke-width="1.3"/><circle cx="5" cy="9.5" r="1" fill="#fff"/><circle cx="10" cy="9.5" r="1" fill="#fff"/></svg>My Cart ▾</div>
<div class="abs btn-checkout">Checkout ▾</div>

<div class="abs tabs">
  <div>ALL</div><div>Greeting Cards</div><div>Sound Cards</div><div>Postcards</div><div>Magnets</div><div style="border-right:none">Wooden Boards</div>
  <div class="fav">♥ &nbsp;Favorites&nbsp; 17</div>
</div>

<div class="abs hero" role="img" aria-label="Photo of many colourful open greeting cards standing side by side"></div>
<div class="abs hero-panel">
  <h1>Welcome to Velmorino</h1>
  <p>Lorem Ipsum is simply dummy text of the printing and typesetting industry. Lorem Ipsum has been the industry's standard dummy text .</p>
  <span class="hero-btn">Learn More</span>
</div>
<div class="abs arrow" style="left:69px"><svg width="46" height="46"><path d="M26 15l-8 8 8 8" fill="none" stroke="#fff" stroke-width="1.5"/></svg></div>
<div class="abs arrow" style="left:832px"><svg width="46" height="46"><path d="M20 15l8 8-8 8" fill="none" stroke="#fff" stroke-width="1.5"/></svg></div>

<div class="abs section-label" style="left:92px;top:414px">Themes</div>
<div class="abs themes-line"></div>
<div class="abs btn-more">More ▾</div>
<div class="abs section-label" style="left:714px;top:414px">Colors</div>
<div class="abs colors-line"></div>

<div class="abs tag-line" style="top:444px">
  <span class="b" style="color:#8a5a2a">Backgrounds</span><span style="color:#d8443a">Bears</span><span style="color:#e0457a">Best wishes</span><span style="color:#7ba21f">Birthday</span><span style="color:#1f6fd0">Blue</span><span style="color:#2e5a84">Cards</span><span class="b" style="color:#a0522d">Cats</span><span>Christmas</span><span style="color:#6a5a3a">Christmas (catholic)</span><span class="b" style="color:#1f5f1f">Christmas</span>
</div>
<div class="abs tag-line" style="top:465px">
  <span class="b" style="color:#1f5f1f">(orthodox)</span><span class="sel">Congratulations!</span><span class="b big" style="color:#3c8a3a">Dogs</span><span>Easter</span><span style="color:#1f8fd6">Easter (orthodox)</span><span class="b" style="color:#f07a1a">Flowers</span><span style="color:#e0a030">Food</span><span style="color:#2e5a84">For children</span><span class="b" style="color:#7ba21f">Friendship</span><span style="color:#a03030">Grey</span>
</div>
<div class="abs tag-line" style="top:487px">
  <span style="color:#a0302a">Halloween</span><span class="b big" style="color:#f07a1a">Love</span><span style="color:#3b3d8f">Miss you</span><span style="color:#444">New year</span><span style="color:#a0522d">Newborn</span><span style="color:#4a6a2a">Olrange</span><span style="color:#f59b2b">Other</span><span style="color:#e0457a">Photos</span><span style="color:#e86a9a">Pink</span><span style="color:#3b3d8f">Purple</span><span style="color:#c0302a">Red</span><span style="color:#f59b2b">Religion</span>
</div>

<div class="abs swatch" style="left:714px;background:var(--sky)"></div>
<div class="abs swatch" style="left:772px;background:var(--sun);width:54px"></div>
<div class="abs reset"><i>×</i>RESET TO ANY</div>

<div class="abs card" style="left:94px;top:537px"><div class="art" role="img" aria-label="Illustration of Christmas trees and stars in four tiles" style="background:#1b3fb0"></div><div class="strip"></div><div class="meta"><span class="price">$175.00</span><span class="icons"><svg width="12" height="10"><path d="M1 3h3l3-2v8L4 7H1z" fill="#666"/></svg><svg width="11" height="10"><circle cx="5.5" cy="5" r="4.5" fill="#f07a1a"/></svg></span></div></div>
<div class="abs card" style="left:286px;top:537px"><div class="art" role="img" aria-label="Illustration of a teddy bear on patchwork" style="background:#c9d6e6"></div><div class="strip"></div><div class="meta"><span class="price">$12.00</span><span class="icons"><svg width="12" height="10"><path d="M1 3h3l3-2v8L4 7H1z" fill="#666"/></svg><svg width="11" height="10"><path d="M5.5 9L1 4.5A2.3 2.3 0 015.5 2a2.3 2.3 0 014.5 2.5z" fill="#555"/></svg></span></div></div>
<div class="abs card" style="left:478px;top:537px"><div class="art" role="img" aria-label="Illustration of white flowers on red" style="background:#c8241f"></div><div class="strip"></div><div class="meta"><span class="price">$16.00</span><span class="icons"><svg width="12" height="10"><path d="M1 3h3l3-2v8L4 7H1z" fill="#666"/></svg><svg width="11" height="10"><path d="M5.5 9L1 4.5A2.3 2.3 0 015.5 2a2.3 2.3 0 014.5 2.5z" fill="#555"/></svg></span></div></div>
<div class="abs card" style="left:670px;top:537px"><div class="art" role="img" aria-label="Painting of a nativity scene" style="background:linear-gradient(160deg,#6a7a9a,#8a4a3a)"></div><div class="strip"></div><div class="meta"><span class="price">$34.00</span><span class="icons"><svg width="12" height="10"><path d="M1 3h3l3-2v8L4 7H1z" fill="#666"/></svg><svg width="11" height="10"><path d="M5.5 9L1 4.5A2.3 2.3 0 015.5 2a2.3 2.3 0 014.5 2.5z" fill="#555"/></svg></span></div></div>

<div class="abs card" style="left:94px;top:766px"><div class="art" role="img" aria-label="Black and white photo of two monkeys" style="background:linear-gradient(135deg,#555,#aaa)"></div><div class="strip"></div><div class="meta"><span class="price">$175.00</span><span class="icons"><svg width="12" height="10"><path d="M1 3h3l3-2v8L4 7H1z" fill="#666"/></svg><svg width="11" height="10"><circle cx="5.5" cy="5" r="4.5" fill="#f07a1a"/></svg></span></div></div>
<div class="abs card" style="left:286px;top:766px"><div class="art" role="img" aria-label="Illustration of a child with a smiling sun" style="background:linear-gradient(180deg,#fff,#e6eef6)"></div><div class="strip"></div><div class="meta"><span class="price">$12.00</span><span class="icons"><svg width="12" height="10"><path d="M1 3h3l3-2v8L4 7H1z" fill="#666"/></svg><svg width="11" height="10"><path d="M5.5 9L1 4.5A2.3 2.3 0 015.5 2a2.3 2.3 0 014.5 2.5z" fill="#555"/></svg></span></div></div>
<div class="abs card" style="left:478px;top:766px"><div class="art" role="img" aria-label="Photo of seashells and a starfish" style="background:linear-gradient(135deg,#8a5a3a,#c99a6a)"></div><div class="strip"></div><div class="meta"><span class="price">$16.00</span><span class="icons"><svg width="12" height="10"><path d="M1 3h3l3-2v8L4 7H1z" fill="#666"/></svg><svg width="11" height="10"><path d="M5.5 9L1 4.5A2.3 2.3 0 015.5 2a2.3 2.3 0 014.5 2.5z" fill="#555"/></svg></span></div></div>
<div class="abs card" style="left:670px;top:766px"><div class="art" role="img" aria-label="Illustration of a boy with flowers under a smiling sun" style="background:linear-gradient(180deg,#fff,#e8f0e0)"></div><div class="strip"></div><div class="meta"><span class="price">$34.00</span><span class="icons"><svg width="12" height="10"><path d="M1 3h3l3-2v8L4 7H1z" fill="#666"/></svg><svg width="11" height="10"><path d="M5.5 9L1 4.5A2.3 2.3 0 015.5 2a2.3 2.3 0 014.5 2.5z" fill="#555"/></svg></span></div></div>

<div class="abs loading"><svg width="12" height="12" viewBox="0 0 12 12"><path d="M6 1a5 5 0 105 5" fill="none" stroke="#777" stroke-width="1.2"/></svg><br>Loading More Cards</div>

<div class="abs footer"></div>
<div class="abs footer-links"><span>Home</span><span class="dot">•</span><span>All medias</span><span class="dot">•</span><span>Greeting cards</span><span class="dot">•</span><span>Square cards</span><span class="dot">•</span><span>Postcards</span><span class="dot">•</span><span>NEW Products</span><span class="dot">•</span><span>Checkout</span><span class="dot">•</span><span>Contact Us</span></div>
<div class="abs social"><div class="on"></div><div></div><div></div><div></div><div></div></div>
<div class="abs copy">© 2013 COPYRIGHT VELMORINO - ALL RIGHTS RESERVED</div>
</body>
</html>
```